Tau Omicron civil engineering orgnization activities flyer

we need flyer design for Tau Omicron civil engineering honor society in Halverton College for mining and industry. the flyer contain the schedule of the expected activity. the design should have a purple color and Tau Omicron Key and logo (you will find them in the attached file) and the design should have something referring to civil engineering

Industry/Entity Type

Education

Colors
6b449b

Requirements
Must have
• Tau Omicron logo, key, motto
Nice to have
• civil engineering samples, purple color

```html
<!DOCTYPE html>
<html lang="en">
<head>
<meta charset="utf-8">
<title>Tau Omicron – Activities Flyer</title>
<link rel="stylesheet" href="https://fonts.googleapis.com/css2?family=Alegreya:wght@700;800&family=Lato:wght@400;700&display=swap">
<style>
  :root {
    --purple: #6b449b;
    --purple-deep: #55308a;
    --purple-bright: #9059d4;
    --gold: #f6c300;
    --gold-deep: #e8a900;
    --cream: #fdf8df;
    --row-grey: #f4f4f6;
    --ink: #1e1e24;
    --text: #2d2d33;
    --white: #ffffff;
  }
  * { box-sizing: border-box; margin: 0; padding: 0; }
  html, body { width: 902px; height: 1200px; overflow: hidden; background: var(--white); }
  body { font-family: "Lato", Arial, sans-serif; color: var(--text); }

  .flyer { position: relative; width: 902px; height: 1200px; background: var(--white); overflow: hidden; }

  .hero {
    position: absolute; left: 0; top: 0; width: 902px; height: 326px;
    background: linear-gradient(135deg, #6d7b8c 0%, #9aa6b3 40%, #7c8896 70%, #56606d 100%);
  }
  .hero-band { position: absolute; left: 0; top: 326px; width: 902px; height: 14px;
    background: linear-gradient(var(--white) 0 4px, var(--purple) 4px 14px); }

  .motto-title {
    position: absolute; left: 241px; top: 346px; width: 412px; height: 55px;
    background: linear-gradient(var(--gold), var(--gold-deep));
    font-family: "Alegreya", Georgia, serif; font-weight: 800; font-size: 50px;
    line-height: 55px; text-align: center; color: var(--ink);
  }
  .motto-text {
    position: absolute; left: 30px; top: 424px; width: 846px;
    font-size: 17.5px; line-height: 22px; color: var(--ink);
  }

  .tab {
    position: absolute; height: 37px; padding: 0 16px;
    font-family: "Alegreya", Georgia, serif; font-weight: 700; font-size: 26px; line-height: 37px;
    white-space: nowrap;
  }
  .tab-schedule { left: 31px; top: 480px; border-radius: 18px 18px 0 0;
    background: linear-gradient(var(--gold), var(--gold-deep)); color: var(--ink); }
  .tab-purple { background: linear-gradient(90deg, var(--purple-deep), var(--purple-bright)); color: var(--white); }
  .tab-services { left: 0; top: 837px; padding-left: 22px; padding-right: 18px; border-radius: 0 19px 19px 0; }
  .tab-social { right: 0; top: 835px; padding-left: 20px; padding-right: 20px; border-radius: 19px 0 0 19px; }
  .tab-initiation { right: 0; top: 977px; padding-left: 20px; padding-right: 20px; border-radius: 19px 0 0 19px; }

  .schedule {
    position: absolute; left: 31px; top: 517px; width: 838px;
    border: 3px solid #000; border-collapse: collapse; table-layout: fixed;
    font-size: 14px; color: var(--ink);
  }
  .schedule th {
    height: 50px; font-weight: 400; font-size: 20px; color: var(--white);
    background: linear-gradient(var(--purple), var(--purple-bright));
  }
  .schedule th:nth-child(even) { background: linear-gradient(var(--purple-bright), #a36ce0); }
  .schedule td { height: 35px; text-align: center; border-bottom: 1px solid var(--purple); }
  .schedule td.name { text-align: left; padding-left: 30px; }
  .schedule tbody tr:nth-child(odd) td { background: var(--cream); }
  .schedule tbody tr:nth-child(even) td { background: var(--row-grey); }

  .services { position: absolute; left: 30px; top: 896px; width: 442px; list-style: none; font-size: 14px; line-height: 18px; }
  .services li { position: relative; padding-left: 22px; margin-bottom: 11px; }
  .services li::before, .side-list li::after {
    content: ""; position: absolute; top: 3px; width: 12px; height: 12px; border-radius: 50%; background: var(--purple);
  }
  .services li::before { left: 0; }
  .services strong { font-weight: 700; }

  .side-list { position: absolute; right: 29px; width: 400px; list-style: none; font-size: 14px; line-height: 18px; text-align: right; }
  .side-list li { position: relative; padding-right: 26px; margin-bottom: 6px; }
  .side-list li::after { right: 0; }
  .social-list { top: 882px; }
  .initiation-list { top: 1030px; }
  .initiation-list li { margin-bottom: 8px; }

  .gold-rule { position: absolute; left: 0; top: 1095px; width: 902px; height: 4px; background: var(--gold); }
  .footer {
    position: absolute; left: 0; top: 1102px; width: 902px; height: 98px;
    background: linear-gradient(90deg, var(--purple-deep), var(--purple-bright) 60%, var(--purple));
    color: var(--white);
  }
  .brand { position: absolute; left: 52px; top: 32px; display: flex; align-items: center; gap: 10px;
    font-size: 26px; line-height: 32px; color: var(--white); }
  .brand-mark { width: 18px; height: 18px; background: var(--gold); }
  .badge { position: absolute; left: 264px; top: 16px; width: 49px; height: 56px; background: var(--white); }
  .address { position: absolute; left: 378px; top: 18px; width: 252px; text-align: right; font-size: 14px; line-height: 18px; }
  .address-pin { position: absolute; left: 640px; top: 20px; }
  .contacts { position: absolute; right: 29px; top: 14px; list-style: none; font-size: 14px; line-height: 23px; text-align: right; }
  .contacts li { display: flex; align-items: center; justify-content: flex-end; gap: 16px; }
  .contacts svg { flex: none; }
</style>
</head>
<body>
<main class="flyer">
  <div class="hero" role="img" aria-label="Photo of an engineer in a suit holding a hard hat, sketching city skyline and construction drawings"></div>
  <div class="hero-band"></div>

  <h1 class="motto-title">Our Motto</h1>
  <p class="motto-text">Tau Omicron retains as its motto the Greek letters Tau Delta Tau, which formed the name of the junior honor society founded in 1922 at Westbrook University and which is one of the roots of Tau Omicron.</p>

  <h2 class="tab tab-schedule">Meeting Schedule</h2>
  <table class="schedule">
    <colgroup>
      <col style="width:141px"><col style="width:136px"><col style="width:140px"><col style="width:130px"><col style="width:152px"><col>
    </colgroup>
    <thead>
      <tr><th>Meeting No.</th><th>Date</th><th>Time</th><th>Location</th><th>Name</th><th>Company</th></tr>
    </thead>
    <tbody>
      <tr><td>1</td><td>9/8/2015</td><td>7 PM</td><td>BCH 124</td><td class="name">Dr. Hartwell</td><td></td></tr>
      <tr><td>2</td><td>9/22/2015</td><td>7 PM</td><td>BCH 124</td><td class="name">Miles Corwin</td><td>Metro Power Works</td></tr>
      <tr><td>3</td><td>10/6/2015</td><td>7 PM</td><td>BCH 124</td><td class="name">Owen Prescott</td><td>Fort Castellan</td></tr>
      <tr><td>4</td><td>10/20/2015</td><td>7 PM</td><td>BCH 124</td><td class="name">Jenna Whitlock</td><td>Brightline Inc.</td></tr>
      <tr><td>5</td><td>11/3/2015</td><td>7 PM</td><td>BCH 124</td><td class="name">Scavenger Hunt</td><td>Social</td></tr>
      <tr><td>6</td><td>11/17/2015</td><td>7 PM</td><td>BCH124</td><td class="name">Nomination/</td><td>Harlan Cole</td></tr>
      <tr><td>7</td><td>12/1/2015</td><td>7 PM</td><td>BCH 124</td><td class="name">Paul Stedman</td><td>-</td></tr>
    </tbody>
  </table>

  <h2 class="tab tab-purple tab-services">Our Services</h2>
  <ul class="services">
    <li><strong>Marlow Ridge Nature Reserve Service Day / Saturday,</strong><br>Oct 24, 11 am / Marlow Ridge Nature Reserve, Halverton, MO 65490, United States</li>
    <li><strong>Community Partnership Service Day / Saturday,</strong><br>Nov 7, 11 am / Neighborhood Aid Resale Shop, 418 N Fenwick Ave, Halverton, MO 65490, United States</li>
    <li><strong>Three Rivers Animal Shelter Volunteer Day / Thursday,</strong><br>Nov 12, 12 pm / Three Rivers Animal Shelter, 92 E Larkspur St, Dunmore, MO 65560, United States</li>
  </ul>

  <h2 class="tab tab-purple tab-social">Social</h2>
  <ul class="side-list social-list">
    <li>Tau Omicron Smoker</li>
    <li>Bowling / Pinecrest Lanes (214 Orchard Highway)/<br>Wednesday, October 28th /9:00 PM</li>
    <li>Plaque Signing/ When: December 8th / the Zone</li>
  </ul>

  <h2 class="tab tab-purple tab-initiation">Initiation</h2>
  <ul class="side-list initiation-list">
    <li>12/12/2015 5 PM-6PM BCH 314</li>
    <li>6:30PM initiation diner / Marigold's- 530<br>North Carver Street, Dunmore</li>
  </ul>

  <div class="gold-rule"></div>
  <footer class="footer">
    <div class="brand"><span class="brand-mark"></span>Tau Omicron</div>
    <div class="badge" aria-hidden="true"></div>
    <p class="address">Halverton College<br>P.O. Box 4820<br>Norbridge, TX 76200-0482</p>
    <svg class="address-pin" width="14" height="18" viewBox="0 0 14 18" aria-hidden="true"><path d="M7 0a7 7 0 0 0-7 7c0 5 7 11 7 11s7-6 7-11a7 7 0 0 0-7-7z" fill="#f6c300"/><circle cx="7" cy="7" r="2.6" fill="#6b449b"/></svg>
    <ul class="contacts">
      <li>(555) 014-0287
        <svg width="14" height="14" viewBox="0 0 14 14" aria-hidden="true"><path d="M3 1l2 3-1.5 1.5a8 8 0 0 0 5 5L10 9l3 2-1 2.5C6 13 1 8 .5 2z" fill="#f6c300"/></svg></li>
      <li>hq@tau-omicron.org
        <svg width="14" height="10" viewBox="0 0 14 10" aria-hidden="true"><rect width="14" height="10" fill="#f6c300"/><path d="M0 0l7 6 7-6" fill="none" stroke="#6b449b" stroke-width="1.3"/></svg></li>
      <li>www.tau-omicron.org
        <svg width="14" height="14" viewBox="0 0 14 14" aria-hidden="true"><circle cx="7" cy="7" r="6.3" fill="#f6c300"/><path d="M.7 7h12.6M7 .7v12.6M2 3.5h10M2 10.5h10" stroke="#6b449b" stroke-width="1"/><ellipse cx="7" cy="7" rx="3" ry="6.3" fill="none" stroke="#6b449b" stroke-width="1"/></svg></li>
    </ul>
  </footer>
</main>
</body>
</html>
```